Business Card for IT Support Company
Aide Nova
Business Card for IT Support Company - Information Technology
Creative Brief
Professional
Assistance Informatique 24/7
Tél. 0900 417 536
2.50 CHF/min de 8h à 22h et 3.50 CHF/min de 22h à 8h depuis le réseau fixe.
info@aide-nova.ch
http://www.aide-nova.ch
No specific name, this is only a hotline IT support number Business Card (phone number is in the title) in Address box, it's the rates on the Business Number. We will use brivopress . ch as the printing company, here are the exact size in mm they send to me: Business card Size is 85x55mm (But file dimension must be 91x61mm) Colors needs to be send in CMYK, minimum 200 dpi, maximum quality.
- Contrôle à distance PC/MAC - Support technique informatique - Formation / Consulting / Coaching - Infographie / Graphisme - Création de Site Web - Smartphone / Tablette

```html
<!DOCTYPE html>
<html lang="fr">
<head>
<meta charset="utf-8">
<title>Aide Nova – Carte de visite</title>
<link rel="stylesheet" href="https://fonts.googleapis.com/css2?family=Arimo:wght@400;700&family=Russo+One&display=swap">
<style>
  :root {
    --page-bg: #e6e4e1;
    --card-white: #ffffff;
    --card-black: #0d0d0d;
    --brand-red: #e0202b;
    --soft-grey: #bfbfbf;
    --text-dark: #1c1c1c;
    --text-light: #ffffff;
  }
  html, body {
    margin: 0;
    padding: 0;
    width: 1200px;
    height: 900px;
    overflow: hidden;
    background: var(--page-bg);
  }
  .sheet {
    position: relative;
    width: 1200px;
    height: 900px;
  }
  .card {
    position: absolute;
    left: 300px;
    width: 600px;
    height: 388px;
    border-radius: 20px;
    overflow: hidden;
    box-shadow: 0 6px 18px rgba(0,0,0,0.18);
  }
  .card--front { top: 46px; background: var(--card-white); }
  .card--back  { top: 466px; background: var(--card-black); }

  .card__shape {
    position: absolute;
    inset: 0;
    width: 600px;
    height: 388px;
  }

  .brand-mark {
    position: absolute;
    left: 150px;
    top: 52px;
    width: 72px;
    height: 72px;
    border-radius: 50%;
    background: var(--brand-red);
  }
  .brand-name {
    position: absolute;
    left: 28px;
    top: 150px;
    margin: 0;
    font-family: "Arimo", Arial, sans-serif;
    font-weight: 400;
    font-size: 30px;
    color: var(--text-dark);
    letter-spacing: 0.5px;
  }

  .contact {
    position: absolute;
    right: 34px;
    top: 248px;
    text-align: right;
    font-family: "Russo One", "Arial Black", sans-serif;
    line-height: 1;
  }
  .contact__cta {
    display: block;
    color: var(--brand-red);
    font-size: 17px;
    letter-spacing: 1px;
    margin-bottom: 6px;
  }
  .contact__phone {
    display: block;
    color: var(--text-light);
    font-size: 32px;
    letter-spacing: 2px;
    margin-bottom: 12px;
  }
  .contact__line {
    display: block;
    color: var(--text-light);
    font-size: 19px;
    letter-spacing: 1px;
    margin-bottom: 6px;
  }

  .services {
    position: absolute;
    left: 0;
    right: 0;
    top: 40px;
    margin: 0;
    padding: 0;
    list-style: none;
    text-align: center;
    font-family: "Arimo", Arial, sans-serif;
    font-size: 17px;
    line-height: 1.7;
    color: var(--text-light);
  }
</style>
</head>
<body>
<main class="sheet">

  <section class="card card--front" aria-label="Recto de la carte">
    <svg class="card__shape" viewBox="0 0 600 388" aria-hidden="true">
      <path d="M0,232 C150,252 300,262 420,217 C500,187 560,162 600,152 L600,388 L0,388 Z" fill="var(--card-black)"/>
      <path d="M0,206 C150,226 300,236 420,191 C500,161 560,136 600,126" fill="none" stroke="var(--soft-grey)" stroke-width="2"/>
      <path d="M0,218 C150,238 300,248 420,203 C500,173 560,148 600,138" fill="none" stroke="var(--brand-red)" stroke-width="8"/>
      <path d="M0,228 C150,248 300,258 420,213 C500,183 560,158 600,148" fill="none" stroke="var(--card-white)" stroke-width="2"/>
    </svg>

    <span class="brand-mark" aria-hidden="true"></span>
    <h1 class="brand-name">Aide Nova 24/7</h1>

    <div class="contact">
      <span class="contact__cta">CALL US TODAY</span>
      <span class="contact__phone">0900 417 536</span>
      <span class="contact__line">INFO@AIDE-NOVA.CH</span>
      <span class="contact__line">WWW.AIDE-NOVA.CH</span>
    </div>
  </section>

  <section class="card card--back" aria-label="Verso de la carte">
    <ul class="services">
      <li>Contrôle à distance PC/MAC | Support technique informatique</li>
      <li>Formation / Consulting / Coaching | Infographie / Graphisme</li>
      <li>Création de Site Web | Smartphone / Tablette</li>
    </ul>
  </section>

</main>
</body>
</html>
```